Business Card for a finance professional

I need a business card design to introduce myself to a professional networking (mainly banks) and potential companies to hire and remember me. I would like to use black, grey, white and maybe gold/silver colors and maybe something with my initials(R L F P T). The final design should communicate seriousness, profissionalism and something innovative.

The basic informations in the card are: Name, e-mail, phone number and trabnet. (I'm thinking to put some directly short link to my trabnet account or maybe some app - non QR Code - to add my contacts to a phone directly.)

My name is Mariana Lopes Ferreira Pinto dos Reis (I prefer to use only 'Mariana Lopes' or 'Mariana Reis' but i'm open to other suggestions) and I have 26 years old (just if it helps to build based in my age).
Updates

Dear designers, I wish to thank your participation in this project! It was very difficult to choose one! Thank your for your work! Best regards and success. Mariana

Target Market(s)

Potential hires and big companies.

Industry/Entity Type

Finance

Requirements
Must have
• The informations required at the business card are:
Name: Mariana Lopes F. P. dos Reis
Email: mariana.lop.reis@quellomail.com
Phone: +55 61 8493 5710
TrabNet: http://br.trabnet-perfis.com/in/marianalr/
Nice to have
• Modern and innovative look.
I suggest to use the colors black, grey, white, gold and/or silver, but I'm open to other colors.
Should not have
• A message showing that I need to be hired. It's more to "know me and remember me" than "hire me please".

```html
<!DOCTYPE html>
<html lang="en">
<head>
<meta charset="utf-8">
<title>Mariana Lopes – Business Card</title>
<link rel="stylesheet" href="https://fonts.googleapis.com/css2?family=Didact+Gothic&display=swap">
<style>
  :root {
    --backdrop: #a9a9a9;
    --card-black: #121212;
    --paper-top: #c2c2c2;
    --paper-bottom: #fbfbfb;
    --gold-dark: #b06d1c;
    --gold-mid: #d99a3a;
    --gold-light: #f3c562;
    --ink-gold: #e29a3a;
  }
  html, body {
    margin: 0;
    padding: 0;
    overflow: hidden;
  }
  body {
    width: 1200px;
    height: 960px;
    background: var(--backdrop);
    position: relative;
    font-family: "Didact Gothic", "Segoe UI", sans-serif;
  }
  .card {
    position: absolute;
    top: 130px;
    width: 402px;
    height: 696px;
    display: block;
  }
  .card--front { left: 163px; }
  .card--back { left: 637px; }
  .card text {
    font-family: "Didact Gothic", "Segoe UI", sans-serif;
    fill: var(--ink-gold);
  }
  .holder-name { font-size: 15.5px; }
  .contact-line { font-size: 10.6px; }
  .monogram { font-size: 50px; }
  .signature-name { font-size: 19px; }
</style>
</head>
<body>

<svg class="card card--front" viewBox="0 0 335 580" aria-label="Business card front">
  <defs>
    <linearGradient id="paper-fade" x1="0" y1="0" x2="0" y2="1">
      <stop offset="0" stop-color="var(--paper-top)"/>
      <stop offset="0.8" stop-color="var(--paper-bottom)"/>
    </linearGradient>
    <linearGradient id="gold-ribbon" x1="0" y1="0" x2="1" y2="0">
      <stop offset="0" stop-color="var(--gold-dark)"/>
      <stop offset="0.55" stop-color="var(--gold-light)"/>
      <stop offset="0.8" stop-color="var(--gold-mid)"/>
      <stop offset="1" stop-color="var(--gold-dark)"/>
    </linearGradient>
  </defs>
  <rect class="paper" width="335" height="580" fill="url(#paper-fade)"/>
  <path class="wave-ribbon" fill="url(#gold-ribbon)"
        d="M0 379 C 95 384, 160 443, 258 443 C 298 443, 320 428, 335 412
           L335 427 C 318 440, 292 452, 255 452 C 160 452, 100 414, 0 404 Z"/>
  <path class="wave-base" fill="var(--card-black)"
        d="M0 404 C 100 414, 160 452, 255 452 C 292 452, 318 440, 335 427 L335 580 L0 580 Z"/>
  <text class="holder-name" x="167" y="76" text-anchor="middle">Mariana Lopes F. P. dos Reis</text>
  <text class="contact-line" x="313" y="491" text-anchor="end">mariana.lop.reis@quellomail.com</text>
  <text class="contact-line" x="313" y="517" text-anchor="end">Phone: +55 61 8493 5710</text>
  <text class="contact-line" x="313" y="542" text-anchor="end">http://br.trabnet-perfis.com/in/marianalr/</text>
</svg>

<svg class="card card--back" viewBox="0 0 335 580" aria-label="Business card back">
  <defs>
    <linearGradient id="gold-ribbon-back" x1="0" y1="0" x2="1" y2="0">
      <stop offset="0" stop-color="var(--gold-dark)"/>
      <stop offset="0.55" stop-color="var(--gold-light)"/>
      <stop offset="0.8" stop-color="var(--gold-mid)"/>
      <stop offset="1" stop-color="var(--gold-dark)"/>
    </linearGradient>
  </defs>
  <rect class="card-base" width="335" height="580" fill="var(--card-black)"/>
  <path class="wave-ribbon" fill="url(#gold-ribbon-back)"
        d="M0 379 C 95 384, 160 443, 258 443 C 298 443, 320 428, 335 412
           L335 427 C 318 440, 292 452, 255 452 C 160 452, 100 414, 0 404 Z"/>
  <text class="monogram" x="26" y="86" textLength="288" lengthAdjust="spacing">RLFPT</text>
  <text class="signature-name" x="167" y="529" text-anchor="middle">Mariana Lopes</text>
</svg>

</body>
</html>
```